Website Design Required

Our client needs a website built from scratch. The website is called Snaps4Wall and is essentially a website that allows you to upload a photo, order and pay and your photo is printed onto a canvas. A closely related website is http://www.framelyte.co.za/ however this project needs a clean, fresh design that encourages purchases.

Snaps4wall will be a dedicated website which allows users to upload and print a single image for large format printing.

The website flow will consist of the following:

• A landing page will be designed which showcases the product offering and offers simple and easy to understand instructions on how to get a photo up- loaded and delivered to their door.

• An upload page will exist that allows users the ability to upload a photo to the website for printing.

• Once the user has uploaded a photo the website will ensure that the dimensions are good enough for printing onto canvas and advise the user accordingly if it is not suitable.
• Once the photo has passed this validation we will take the user to a new page that will give them a preview of their photo. Here they will be given a chance to place the photo correctly should the need arise.

• Once the user is happy with the photo placement they will click on the next button which will take them to the payment and delivery page whereby they will need to complete all the fields.

• Once done, a final order page will appear confirming all the details of the order as well as payment and delivery information. Once the user is satisfied he can click the order button.

Requirements
Must have
• We will need the following pages designed:
1. Homepage
2. Upload page
3. Photo placement page (which allows users to align their photo onto the canvas)
4. Order & Payment page
Should not have
• The design should not use old style fonts and shoddy illustrations. If illustrations are used they have to be clean, simple, stylish.

```html
<!DOCTYPE html>
<html lang="en">
<head>
<meta charset="utf-8">
<title>Snaps4Wall – Upload photo</title>
<link rel="stylesheet" href="https://fonts.googleapis.com/css2?family=Questrial&family=Arimo:wght@400;700&display=swap">
<style>
  :root{
    --page-bg:#f7f7f7;
    --white:#ffffff;
    --ink:#222222;
    --muted:#9a9a9a;
    --body-text:#6b6b6b;
    --heading-teal:#1d3f50;
    --heading-brown:#4a3a33;
    --banner-dark:#6b4538;
    --banner-mid:#a77766;
    --banner-light:#d9b2a2;
    --box-border:#dedede;
    --field-border:#e6e6e6;
    --blue-top:#3aa9ec;
    --blue-bottom:#1576c4;
    --orange-top:#f57a2c;
    --orange-bottom:#d9480f;
    --red-top:#e0311e;
    --red-bottom:#a9140c;
    --link-orange:#e8811d;
    --footer-bg:#ececec;
    --footer-line:#d4d4d4;
  }
  *{margin:0;padding:0;box-sizing:border-box}
  html,body{width:1200px;height:1025px;overflow:hidden}
  body{background:var(--page-bg);font-family:'Arimo',Arial,sans-serif;color:var(--ink);position:relative}
  .abs{position:absolute}

  .topbar{left:0;top:0;width:1200px;height:68px;background:var(--white)}
  .brand{left:111px;top:0;width:102px;height:143px;background:#111;z-index:3;
    display:flex;align-items:center;justify-content:center}
  .brand-name{font-family:'Questrial',sans-serif;color:var(--white);font-size:17px;letter-spacing:.5px}

  .nav a{position:absolute;top:20px;height:29px;line-height:29px;font-size:15px;color:var(--ink);
    text-decoration:none;text-transform:uppercase;font-family:'Arimo',sans-serif}
  .nav .active{background:#1a1414;color:var(--white);border-radius:4px;width:91px;text-align:center}

  .banner{left:0;top:68px;width:1200px;height:156px;
    background:linear-gradient(90deg,var(--banner-dark) 0%,var(--banner-mid) 45%,var(--banner-mid) 70%,var(--banner-light) 100%)}
  .banner-title{left:111px;top:150px;font-family:'Questrial',sans-serif;font-size:39px;color:var(--white);letter-spacing:1px}
  .banner-art{left:942px;top:118px;width:80px;height:78px;border-radius:6px;
    background:linear-gradient(135deg,#4a7ec4,#1c2c4a)}

  .page-title{left:129px;top:266px;font-family:'Questrial',sans-serif;font-size:26px;color:var(--heading-teal)}

  .upload-box{left:132px;top:333px;width:937px;height:349px;background:var(--white);border:5px solid var(--box-border)}
  .col-title{font-family:'Questrial',sans-serif;font-size:26px;color:var(--heading-brown)}
  .add-link{font-size:13px;color:#b5b5b5;text-decoration:underline}
  .field{height:36px;border:1px solid var(--field-border);background:var(--white);border-radius:2px}
  .browse{width:102px;height:36px;border:1px solid #cfcfcf;border-radius:3px;
    background:linear-gradient(#f6f6f6,#dcdcdc);font-size:13px;color:#333;text-align:center;line-height:34px}
  .hint{font-size:13px;color:var(--muted)}
  .url-label{font-size:14px;font-weight:700;color:#555}
  .hint .learn{color:var(--link-orange)}

  .btn{height:46px;border-radius:4px;color:var(--white);font-size:21px;font-weight:700;text-align:center;line-height:46px}
  .btn-cancel{width:118px;background:linear-gradient(var(--blue-top),var(--blue-bottom))}
  .btn-upload{width:188px;background:linear-gradient(var(--orange-top),var(--orange-bottom))}
  .usage{font-size:13px;color:var(--muted)}
  .usage b{color:var(--link-orange)}

  .intro{left:132px;top:709px;width:563px;font-size:13px;line-height:21.5px;color:var(--body-text);text-align:justify}

  .promo{left:758px;top:713px;width:308px;height:68px;border-radius:3px;
    background:linear-gradient(var(--red-top),var(--red-bottom));color:var(--white);
    font-family:'Arimo',sans-serif;font-weight:700;font-size:23px;line-height:25px;padding:8px 0 0 14px}
  .promo-art{left:990px;top:722px;width:56px;height:46px;border:3px solid #f2e7dc;
    background:linear-gradient(#c9a27e,#7d5637)}

  .footer{left:0;top:917px;width:1200px;height:108px;background:var(--footer-bg);border-top:2px solid var(--footer-line)}
  .copyright{left:64px;top:935px;font-size:13px;color:#777}
  .copyright span{margin:0 10px}
  .social{top:932px;width:25px;height:25px;border-radius:50%}
</style>
</head>
<body>
  <header>
    <div class="abs topbar"></div>
    <div class="abs brand"><span class="brand-name">Snaps4Wall</span></div>
    <nav class="nav">
      <a class="active" style="left:583px">Home</a>
      <a style="left:697px">Upload Photo</a>
      <a style="left:858px">Pricing</a>
      <a style="left:975px">Contat Us</a>
      <a style="left:1099px">Login</a>
    </nav>
    <div class="abs banner"></div>
    <h1 class="abs banner-title" style="font-weight:400">Upload&nbsp; photo</h1>
    <div class="abs banner-art" role="img" aria-label="Camera with a framed photo"></div>
  </header>

  <main>
    <h2 class="abs page-title" style="font-weight:400">Upload photo to Snaps4wall</h2>

    <section class="abs upload-box"></section>

    <div class="abs col-title" style="left:161px;top:362px">Find an image from your computer</div>
    <div class="abs add-link" style="left:163px;top:405px">Add another image</div>
    <div class="abs field" style="left:157px;top:438px;width:299px"></div>
    <div class="abs browse" style="left:465px;top:438px">Browse..</div>
    <div class="abs hint" style="left:162px;top:498px">We accept jpg, gif, bmp and png images, 8 MB maximum size</div>

    <div class="abs col-title" style="left:642px;top:362px">Or add an image from the web</div>
    <div class="abs add-link" style="left:645px;top:405px">Add another image</div>
    <div class="abs url-label" style="left:648px;top:463px">URL</div>
    <div class="abs field" style="left:697px;top:438px;width:299px"></div>
    <div class="abs hint" style="left:646px;top:500px"><span class="learn">Learn more</span> about using web images</div>

    <div class="abs btn btn-cancel" style="left:172px;top:594px">Cancel</div>
    <div class="abs btn btn-upload" style="left:302px;top:594px">Upload Image</div>
    <div class="abs usage" style="left:508px;top:611px">You are currently using 8MB (0%) of your 1024MB &nbsp;<b>?</b></div>

    <p class="abs intro">Lorem ipsum dolor sit amet, consectetuer adipiscing elit. Aenean commodo ligula eget dolor. Aenean massa. Cum sociis natoque penatibus et magnis dis parturient montes, nascetur ridiculus mus. Donec qes nec, pellentesque eu, pretium quis, sem. Nulla consequat massa quis enim. Donec pede justo, fringilla vel, aliqu, vulputaLorem</p>

    <div class="abs promo">FREE DELIVERY<br>IN SA</div>
    <div class="abs promo-art" role="img" aria-label="Framed landscape print"></div>
  </main>

  <footer>
    <div class="abs footer"></div>
    <div class="abs copyright">Copyright © 2011 &nbsp;Snaps4wall.com . All Rights Reserved. &nbsp;Terms &amp; Conditions<span>|</span>Privacy Policy</div>
    <div class="abs social" style="left:1005px;background:#3b5a9a" aria-label="Social link"></div>
    <div class="abs social" style="left:1040px;background:#3a8fd0" aria-label="Social link"></div>
    <div class="abs social" style="left:1076px;background:#f08a1c" aria-label="Social link"></div>
    <div class="abs social" style="left:1112px;background:#d8352a" aria-label="Social link"></div>
  </footer>
</body>
</html>
```